Songs from Elder Ruins

Looking for a cover for a small booklet titled as above volume 1 ,

The cover needs to be Masonic in nature images of perhaps building king solomon a temple perhaps, the tales are poems covering the first 4 degrees in freemasonry.
Author
Dennis P Holt

```html
<!DOCTYPE html>
<html lang="en">
<head>
<meta charset="UTF-8">
<title>Songs from Elder Ruins — Book Cover</title>
<link rel="stylesheet" href="https://fonts.googleapis.com/css2?family=Cinzel:wght@400&family=Cormorant+Garamond:ital,wght@1,500&family=Tinos&display=swap">
<style>
  :root {
    --stage-center: #3b4759;
    --stage-edge: #07111f;
    --stone-light: #a0602c;
    --stone-mid: #6a3a1a;
    --stone-dark: #1c0f08;
    --band-shade: rgba(12, 8, 5, 0.62);
    --gold-rule: #a48a55;
    --gold-bright: #f3e4b5;
    --gold-deep: #8a6a2e;
    --silver-light: #e4e4e4;
    --silver-dark: #6e6e6e;
    --strip-light: #f1e7c4;
    --strip-dark: #c9b57e;
    --ink: #111111;
    --title-white: #ffffff;
  }
  * { margin: 0; padding: 0; box-sizing: border-box; }
  html, body { width: 1200px; height: 1000px; overflow: hidden; }
  body {
    background: radial-gradient(ellipse 55% 70% at 50% 50%, var(--stage-center) 0%, #1a2638 55%, var(--stage-edge) 100%);
    position: relative;
  }
  .book-cover {
    position: absolute;
    left: 288px;
    top: 0;
    width: 624px;
    height: 1000px;
    overflow: hidden;
  }
  .cover-art {
    position: absolute;
    inset: 0 0 128px 0;
    background:
      radial-gradient(ellipse 18% 60% at 52% 70%, rgba(200,120,60,0.55), transparent 70%),
      linear-gradient(90deg, var(--stone-mid) 0%, var(--stone-light) 18%, var(--stone-dark) 40%, var(--stone-dark) 58%, var(--stone-light) 82%, var(--stone-mid) 100%);
  }
  .title-band {
    position: absolute;
    left: 0;
    top: 214px;
    width: 100%;
    height: 388px;
    background: var(--band-shade);
    border-top: 6px solid var(--gold-rule);
    border-bottom: 6px solid var(--gold-rule);
    text-align: center;
  }
  .emblem-area {
    position: absolute;
    z-index: 2;
    left: 222px;
    top: 48px;
    width: 180px;
    height: 196px;
    background: linear-gradient(160deg, var(--silver-light), var(--silver-dark));
    opacity: 0.55;
  }
  .cover-title { display: block; }
  .title-lead,
  .title-main,
  .title-sub { display: block; }
  .title-lead {
    font-family: "Cormorant Garamond", serif;
    font-style: italic;
    font-weight: 500;
    font-size: 98px;
    line-height: 1;
    color: var(--title-white);
    margin-top: 34px;
  }
  .title-main,
  .title-sub {
    font-family: "Cinzel", serif;
    font-weight: 400;
    line-height: 1;
    background: linear-gradient(180deg, var(--gold-bright) 0%, #d6b872 45%, var(--gold-deep) 100%);
    -webkit-background-clip: text;
    background-clip: text;
    color: transparent;
  }
  .title-main {
    font-size: 150px;
    margin-top: 4px;
    letter-spacing: 2px;
  }
  .title-sub {
    font-size: 82px;
    margin-top: 6px;
    letter-spacing: 1px;
  }
  .author-strip {
    position: absolute;
    left: 0;
    bottom: 0;
    width: 100%;
    height: 128px;
    background: linear-gradient(90deg, var(--strip-dark) 0%, var(--strip-light) 35%, var(--strip-light) 65%, var(--strip-dark) 100%);
    border-top: 3px solid #222;
    display: flex;
    align-items: center;
    justify-content: center;
  }
  .author-name {
    font-family: "Tinos", serif;
    font-size: 80px;
    color: var(--ink);
    letter-spacing: 1px;
  }
</style>
</head>
<body>
  <main class="book-cover">
    <div class="cover-art" role="img" aria-label="Photograph of a narrow ancient stone passage lit in warm amber tones"></div>
    <header class="title-band">
      <h1 class="cover-title">
        <span class="title-lead">Songs from</span>
        <span class="title-main">ELDER</span>
        <span class="title-sub">RUINS</span>
      </h1>
    </header>
    <div class="emblem-area" role="img" aria-label="Silver metallic emblem ornament above the title"></div>
    <footer class="author-strip">
      <p class="author-name">Dennis P Holt</p>
    </footer>
  </main>
</body>
</html>
```